Long Established Local Fencing (not swords) Business needs fresh Business Cards

We need fresh double sided business cards for our Fencing Construction business, we are looking for something with our new logo design added, and maybe a photo background ?
We recently had cards made from Cardlyne and we were horrified with what we got back, the quality was terrible, so am looking for high quality format for good printing company to make.
We install Steelmora, Timber paling, Aluminium Slat Screening, Picket (timber and aluminium) and most other fencing installations.
Our website is brankelrails.com.au should you like to learn a bit more.
We do have logo in other formats if required.
We have been in business for over 35 years and we have used this as a "motto" it is on our signage

Industry/Entity Type

Construction

Contact Information for Business Card

Open to ideas, we need 3 x different cards, one generic with no name and 2 x others each with 1 of our bosses name on each, I will put into upload files.

Colors
ec1f27
000000
606060
f5f5f5

Requirements
Must have
• Company Name and Logo
• Address
• Contact details, phone, website, email etc
• Small space to write notes when leaving card at residence
Nice to have
• Our motto "Servicing the Peninsula for over 35 years"

```html
<!DOCTYPE html>
<html lang="en">
<head>
<meta charset="utf-8">
<title>Brankel Rails – Business Cards</title>
<link href="https://fonts.googleapis.com/css2?family=Archivo:wght@500;600;700;800&family=Archivo+Narrow:ital,wght@1,700&display=swap" rel="stylesheet">
<style>
  :root {
    --red: #ec1f27;
    --black: #000000;
    --grey: #606060;
    --light: #f5f5f5;
    --white: #ffffff;
    --stage: #e4e4e4;
    --steel-dark: #2f3338;
    --steel-mid: #5b6168;
    --hedge: #3f5a2c;
  }
  * { box-sizing: border-box; margin: 0; padding: 0; }
  html, body { width: 1200px; height: 900px; overflow: hidden; }
  body {
    background: var(--stage);
    font-family: "Archivo", Arial, sans-serif;
    position: relative;
  }
  .card {
    position: absolute;
    width: 660px;
    height: 400px;
    border-radius: 26px;
    overflow: hidden;
    background: var(--white);
    box-shadow: 0 10px 28px rgba(0,0,0,.22);
  }
  /* Front */
  .card--front { left: 130px; top: 30px; }
  .motto-band {
    height: 62px;
    display: flex;
    align-items: center;
    justify-content: center;
    background: var(--white);
  }
  .motto {
    font-family: "Archivo Narrow", "Arial Narrow", sans-serif;
    font-style: italic;
    font-weight: 700;
    font-size: 27px;
    letter-spacing: .5px;
    color: var(--red);
    text-transform: uppercase;
  }
  .fence-photo {
    position: absolute;
    left: 0; right: 0; top: 62px; bottom: 0;
    background:
      linear-gradient(180deg, rgba(0,0,0,0) 70%, var(--hedge) 100%),
      linear-gradient(90deg, var(--steel-mid) 0%, var(--steel-dark) 45%, var(--steel-mid) 100%);
  }
  .brand-tile {
    position: absolute;
    left: 230px; top: 120px;
    width: 200px; height: 180px;
    background: var(--white);
    display: flex;
    align-items: center;
    justify-content: center;
    gap: 10px;
    box-shadow: 0 2px 8px rgba(0,0,0,.25);
  }
  .brand-mark { width: 16px; height: 16px; background: var(--red); flex: none; }
  .brand-name {
    font-weight: 800;
    font-size: 24px;
    line-height: 1.05;
    color: var(--black);
    text-transform: uppercase;
  }
  /* Back */
  .card--back { left: 410px; top: 470px; background: linear-gradient(135deg, var(--white) 40%, var(--light) 100%); }
  .card--back .brand {
    position: absolute;
    right: 34px; top: 40px;
    display: flex; align-items: center; gap: 10px;
  }
  .card--back .brand-name { font-size: 34px; }
  .holder-name {
    position: absolute; left: 52px; top: 118px;
    font-weight: 700; font-size: 38px; line-height: 1.15; color: var(--red);
  }
  .mobile {
    position: absolute; left: 54px; top: 166px;
    font-weight: 600; font-size: 20px; line-height: 1.2; color: var(--black);
  }
  .mobile .label { color: var(--red); }
  .note-lines {
    position: absolute; left: 54px; top: 198px;
    width: 380px;
  }
  .note-lines span {
    display: block; height: 32px;
    border-bottom: 1.5px solid var(--black);
  }
  .office-phone {
    position: absolute; left: 52px; top: 310px;
    font-weight: 700; font-size: 42px; color: var(--red); line-height: 1;
  }
  .website {
    position: absolute; left: 54px; top: 358px;
    font-weight: 700; font-size: 20px; line-height: 1.2; color: var(--black);
  }
  .address {
    position: absolute; right: 40px; top: 226px;
    font-style: normal;
    font-weight: 600; font-size: 18px; line-height: 1.3; color: var(--black);
  }
</style>
</head>
<body>

<section class="card card--front">
  <div class="motto-band"><p class="motto">Servicing the Peninsula for over 35 years</p></div>
  <div class="fence-photo" role="img" aria-label="Photo of a dark steel sheet fence with green hedge along its base"></div>
  <div class="brand-tile">
    <span class="brand-mark"></span>
    <p class="brand-name">Brankel<br>Rails</p>
  </div>
</section>

<section class="card card--back">
  <div class="brand">
    <span class="brand-mark"></span>
    <p class="brand-name">Brankel Rails</p>
  </div>
  <h1 class="holder-name">Darren Colbeck</h1>
  <p class="mobile"><span class="label">m</span> 041 527 3084</p>
  <div class="note-lines"><span></span><span></span><span></span></div>
  <p class="office-phone">02 4388 1520</p>
  <p class="website">www.brankelrails.com.au</p>
  <address class="address">42 Tidewater Road<br>Brankel<br>Nsw 2259</address>
</section>

</body>
</html>
```